Redesign for luxury lifestyle PR agency

Ginger Kite Otter is a luxury lifestyle public relations agency specialising in indigenous and regenerative travel. We are the elephant you want in the room. We represent interesting brands and people who would be described as changemakers in their respective fields. The winning design should be stylish, clean cut and earthy. It should communicate that Ginger Kite Otter is professional and representative of the industries that it serves. The purpose of the website is to provide clear information to potential customers and media, improve the image and brand of the company, position the company as one of scale and increase sales conversions. Its aesthetic will be aspirational and image led in an editorial style. I would like to be able to easily edit the website once finished and be able to work with the designer on an ad hoc basis once the project is completed.

Please see below for some website I like the style of:

https://www.velmora-ensemble.com/

https://www.tasbergglobal.com/

https://www.brindlequarterly.co.uk/

Pages I would like to include are:

Home
Services
Clients
Testimonials
About Us
News

I'm also attaching a proposal that I really liked the style of and I would like this sort of aesthetic on the website too. My logo is also attached (it is likely that the colour palette might change with the website).

I'm open to inspiration on the colours - my immediate preference is greens and/or blues.

Here is the existing website that I built myself on Wix - https://www.gingerkiteotter.com/ (it looks so outdated and amateur now hence the need of a serious rebrand)

Target Market(s)

Luxury travel and lifestyle brands

Industry/Entity Type

Luxury travel and lifestyle

Number of Pages Required

1 page

Font styles to use
Serif
Other font styles liked:
• Open to suggestions

Requirements
Must have
• Beautiful imagery

```html
<!DOCTYPE html>
<html lang="en">
<head>
<meta charset="utf-8">
<title>Ginger Kite Otter — Lifestyle PR</title>
<link href="https://fonts.googleapis.com/css2?family=Playfair+Display:wght@400;700&family=Montserrat:wght@300;400&display=swap" rel="stylesheet">
<style>
:root{
  --paper:#ffffff;
  --sand:#eeede3;
  --sand-line:#dcdbd0;
  --ink:#5c5b53;
  --ink-soft:#8a897f;
  --charcoal:#3e3d44;
  --serif:'Playfair Display', Georgia, serif;
  --sans:'Montserrat', Arial, sans-serif;
}
*{margin:0;padding:0;box-sizing:border-box}
html,body{width:1200px;height:5136px;overflow:hidden;background:var(--paper)}
body{position:relative;font-family:var(--serif);color:var(--ink)}
.abs{position:absolute}
.photo{position:absolute}
.section-label{position:absolute;left:0;width:1200px;text-align:center;font-size:13px;color:var(--ink-soft);letter-spacing:.5px}

/* header / hero */
.hero-panel{left:596px;top:0;width:604px;height:672px;background:var(--sand)}
.brand{left:88px;top:30px;display:flex;align-items:center;gap:10px;font-family:var(--sans);font-size:15px;letter-spacing:1.5px;color:var(--ink)}
.brand-dot{width:14px;height:14px;border-radius:50%;background:var(--ink)}
.nav{left:688px;top:40px;display:flex;gap:30px;font-family:var(--sans);font-size:14px;color:var(--ink)}
.hero-photo{left:108px;top:128px;width:408px;height:416px;background:linear-gradient(135deg,#3f5a2e,#6f7f3f 45%,#b58a5e 70%,#4b3a24)}
.hero-title{left:688px;top:166px;width:440px;font-size:38px;font-weight:700;line-height:1.3;letter-spacing:1px;color:#5a5950}
.hero-text{left:688px;top:318px;width:420px;font-family:var(--sans);font-size:17px;line-height:1.65;color:var(--ink-soft)}

/* services */
.services-photo{left:608px;top:876px;width:504px;height:596px;background:linear-gradient(160deg,#3a2a22,#8a5a3a 35%,#c4a27a 55%,#a2282a 70%,#6b5a44)}
.services-card{left:360px;top:928px;width:528px;height:656px;background:rgba(238,237,227,.86)}
.services-kicker{left:392px;top:984px;font-size:20px;letter-spacing:1.5px;color:var(--ink)}
.services-lead{left:392px;top:1044px;width:410px;font-size:19px;line-height:1.45;color:var(--ink-soft)}
.services-list{left:420px;top:1222px;list-style:none;font-size:12px;color:var(--ink)}
.services-list li{height:40px;display:flex;align-items:center;gap:10px}
.services-list b{font-size:18px;font-weight:400}

/* clients intro */
.client-a{left:88px;top:2016px;width:328px;height:328px;background:linear-gradient(150deg,#d8cdb8,#b49a74 50%,#7d6a52)}
.client-b{left:432px;top:2016px;width:332px;height:328px;background:linear-gradient(150deg,#cdb9a2,#a83430 45%,#e9e3da 75%,#8b7560)}
.client-card{left:784px;top:2016px;width:328px;height:328px;background:var(--sand)}
.client-kicker{left:0;top:32px;width:328px;text-align:center;font-size:12px;color:var(--ink-soft)}
.client-text{left:24px;top:70px;width:290px;font-size:21px;font-weight:700;line-height:1.55;color:#55544c}
.client-arrow{left:24px;top:210px}

/* testimonial */
.quote-box{left:88px;top:2388px;width:688px;height:324px;background:var(--sand);border:1px solid var(--sand-line)}
.quote-text{left:110px;top:92px;width:470px;text-align:center;font-size:13px;font-style:italic;line-height:1.7;color:var(--ink-soft)}
.quote-prev{left:22px;top:146px}
.quote-next{left:648px;top:146px}
.quote-photo{left:776px;top:2388px;width:336px;height:324px;background:linear-gradient(180deg,#8fb6d6 0%,#bcd3e2 30%,#d9c7a8 55%,#4f7f9a 80%,#2f5c78)}

/* about */
.about-block{left:664px;top:2964px;width:400px;height:452px;background:var(--charcoal)}
.about-portrait{left:612px;top:3068px;width:292px;height:352px;background:linear-gradient(160deg,#e4e4e4,#8c8c8c 55%,#3a3a3a)}
.about-text{left:160px;top:3066px;width:400px;font-size:13px;line-height:1.75;color:var(--ink)}
.about-text p+p{margin-top:18px}

/* gallery */
.gallery{left:0;width:1200px;display:flex;gap:8px}
.gallery div{height:224px;flex:none}
.row-1{top:3752px}
.row-2{top:3988px}

/* blog */
.post{top:4456px;width:280px}
.post-image{height:168px}
.post-meta{margin-top:16px;font-size:11px;color:var(--ink-soft)}
.post-title{margin-top:8px;font-size:15px;font-weight:700;line-height:1.35;color:#4e4d46}
.post-excerpt{margin-top:10px;font-size:11px;line-height:1.6;color:var(--ink-soft)}
.post-more{margin-top:14px;font-size:11px;color:var(--ink-soft)}

/* footer */
.footer{left:0;top:5060px;width:1200px;font-size:12px;color:var(--ink-soft)}
.footer-email{position:absolute;left:172px;top:32px}
.footer-contact{position:absolute;left:0;width:1200px;text-align:center;line-height:1.55}
.footer-phone{position:absolute;left:920px;top:32px}
</style>
</head>
<body>

<header>
  <div class="abs hero-panel"></div>
  <div class="abs brand"><span class="brand-dot"></span>GINGER KITE OTTER</div>
  <nav class="abs nav"><span>Home</span><span>Services</span><span>clients</span><span>Who we are</span><span>Contacts</span></nav>
</header>

<section class="hero">
  <div class="photo hero-photo" role="img" aria-label="Hand reaching into a leafy tree with ripening fruit"></div>
  <h1 class="abs hero-title">The Elephant You Want In The Room</h1>
  <p class="abs hero-text">Ginger Kite Otter is a boutique lifestyle PR and communications agency helping brands get their voices heard in the UK.</p>
</section>

<section class="services">
  <div class="section-label" style="top:804px">Services</div>
  <div class="photo services-photo" role="img" aria-label="Elegant table setting with champagne glass and red napkin"></div>
  <div class="abs services-card"></div>
  <h2 class="abs services-kicker">PURE AND SIMPLE</h2>
  <p class="abs services-lead">No nonsense approach to launching new brands to the UK market, offering a completely bespoke service to include:</p>
  <ul class="abs services-list">
    <li><b>1</b>Strategic Planning</li>
    <li><b>2</b>Consumer Media Relations</li>
    <li><b>3</b>Stakeholder Management</li>
    <li><b>4</b>Influencer Engagement</li>
    <li><b>5</b>Creative Consultation</li>
  </ul>
</section>

<section class="clients-intro">
  <div class="photo client-a" role="img" aria-label="Dried grasses and woven textures"></div>
  <div class="photo client-b" role="img" aria-label="Hands in embroidered traditional dress"></div>
  <div class="abs client-card">
    <div class="abs client-kicker">Clients</div>
    <p class="abs client-text">A dynamic collection of innovative lifestyle clients that we are wholly passionate about</p>
    <svg class="abs client-arrow" width="24" height="12" viewBox="0 0 24 12"><path d="M23 6H2M7 1 2 6l5 5" fill="none" stroke="#55544c" stroke-width="1.4"/></svg>
  </div>
</section>

<section class="testimonial">
  <div class="abs quote-box">
    <svg class="abs quote-prev" width="14" height="24" viewBox="0 0 14 24"><path d="M12 2 2 12l10 10" fill="none" stroke="#6b6a62" stroke-width="1.5"/></svg>
    <p class="abs quote-text">"Working with the team has been a genuine pleasure from the very first call. Their care, calm judgement and deep media ties gave our launch real reach, and every story felt true to who we are. We could not ask for better partners."</p>
    <svg class="abs quote-next" width="14" height="24" viewBox="0 0 14 24"><path d="M2 2l10 10L2 22" fill="none" stroke="#6b6a62" stroke-width="1.5"/></svg>
  </div>
  <div class="photo quote-photo" role="img" aria-label="Colourful waterfront houses beside a calm bay"></div>
  <div class="section-label" style="top:2776px">Testimonials</div>
</section>

<section class="about">
  <div class="section-label" style="top:2916px">Who We Are</div>
  <div class="abs about-block"></div>
  <div class="photo about-portrait" role="img" aria-label="Black and white portrait of the agency founder"></div>
  <div class="abs about-text">
    <p>Maren Hollis founded Ginger Kite Otter in 2016 after working for one of the most reputable luxury travel PR agencies in London, leading a team that launched some of the world's most loved hotels and spending time as a national newspaper writer. She understands what it is like to be on either side of the PR coin and what it takes to create a juicy story.</p>
    <p>Ginger Kite Otter works as an extension to your team, providing a service that feels in-house. Maren offers a direct approach and will always pick up the phone to ensure an undiluted and candid view while you're planning for future success. The Ginger Kite Otter clients are a carefully curated list and they feel like family.</p>
  </div>
</section>

<section class="client-gallery">
  <div class="section-label" style="top:3664px">Our Clients</div>
  <div class="abs gallery row-1">
    <div style="width:248px;background:linear-gradient(150deg,#c9b6a0,#a3302e 50%,#e6ddd1)" role="img" aria-label="Embroidered traditional clothing"></div>
    <div style="width:252px;background:linear-gradient(150deg,#d7b77a,#8a6b3a 55%,#3c4a2e)" role="img" aria-label="Woman in a golden wheat field"></div>
    <div style="width:252px;background:linear-gradient(180deg,#e4c9a4,#9a7a5a 50%,#4c5e6e)" role="img" aria-label="Stone stack at sunset by the sea"></div>
    <div style="width:248px;background:linear-gradient(150deg,#efe7d6,#d8b25a 50%,#a88a56)" role="img" aria-label="Lemons and linen on a table"></div>
    <div style="width:168px;background:linear-gradient(180deg,#9ec1da,#d8c6a8 55%,#4e7e98)" role="img" aria-label="Waterfront village houses"></div>
  </div>
  <div class="abs gallery row-2">
    <div style="width:248px;background:linear-gradient(150deg,#b43a32,#d9a07a 50%,#4f5e6c)" role="img" aria-label="Red boat moored by a harbour"></div>
    <div style="width:252px;background:linear-gradient(150deg,#e3c99c,#6a4a32 55%,#2e2420)" role="img" aria-label="Woman with long hair facing the sunlight"></div>
    <div style="width:252px;background:linear-gradient(180deg,#b9c6cf,#7f7a66 50%,#4a4234)" role="img" aria-label="Rugged mountain landscape"></div>
    <div style="width:248px;background:linear-gradient(150deg,#f1ece4,#cfc5b6 55%,#9e9484)" role="img" aria-label="Folded white linen detail"></div>
    <div style="width:168px;background:linear-gradient(150deg,#ece6da,#c8b79e 55%,#8c7a62)" role="img" aria-label="Woven textile close up"></div>
  </div>
</section>

<section class="blog">
  <div class="section-label" style="top:4372px">Our Blog</div>
  <article class="abs post" style="left:116px">
    <div class="post-image" style="background:linear-gradient(160deg,#e9e4da,#8a2a2a 45%,#3c3a3a)" role="img" aria-label="Dressed dining table with red accents"></div>
    <div class="post-meta">May 14, 2021 | Journal, Lifestyle</div>
    <h3 class="post-title">Lorem ipsum dolor sit amet, consectetur adipiscing elit, sed do</h3>
    <p class="post-excerpt">Notes from a season of quiet travel, where small hosts and slow kitchens shape the stories we love to tell our media friends across the UK each week.</p>
    <div class="post-more">Read More</div>
  </article>
  <article class="abs post" style="left:460px">
    <div class="post-image" style="background:linear-gradient(160deg,#f2efea,#c9c2b8 50%,#6e6458)" role="img" aria-label="Coffee cups on a bright counter"></div>
    <div class="post-meta">May 14, 2021 | Journal, Lifestyle</div>
    <h3 class="post-title">Lorem ipsum dolor sit amet, consectetur adipiscing elit, sed do</h3>
    <p class="post-excerpt">How a thoughtful launch plan helps new brands find their voice, earn trust with editors and build lasting warmth with guests who care about place.</p>
    <div class="post-more">Read More</div>
  </article>
  <article class="abs post" style="left:800px">
    <div class="post-image" style="background:linear-gradient(180deg,#a6c6dd,#dac8a8 55%,#4d7d98)" role="img" aria-label="Seaside village with colourful houses"></div>
    <div class="post-meta">May 14, 2021 | Journal, Lifestyle</div>
    <h3 class="post-title">Lorem ipsum dolor sit amet, consectetur adipiscing elit, sed do</h3>
    <p class="post-excerpt">A short guide to coastal escapes that give back, from family run guesthouses to regenerative farms welcoming curious travellers this coming summer.</p>
    <div class="post-more">Read More</div>
  </article>
</section>

<footer class="abs footer">
  <span class="footer-email">hello@gingerkiteotter.com</span>
  <div class="footer-contact">Contact<br>14 Marlow Lane, London<br>EC2A 4NE</div>
  <span class="footer-phone">+44 20 7946 0182</span>
</footer>

</body>
</html>
```